Corporate Brochure for boutique Australian financial planning firm

We are looking for a face-lift with our company corporate brochure. This brochure will be used to show who we are, what we do, etc. to new potential clients. It will form part of an introductory pack that we give to clients after an initial free consultation.

The target market is generally people over 45 years old, including couples and singles, seeking financial advice.

We have a new logo and would like to implement elements of the logo design into the brochure.

There is a bit of text on the brochure so perhaps 3 double sided A4 pages (6 pages in total) with a trifold might work best.

The colours in our logo are black and red. We are looking to use these colours and maybe also white and grey?

We are after a contemporary, clean, minimalist design using elements/shapes/forms of our logo design in there so it's not generic and speaks out as 'ours'. It needs to be professional but not traditional looking if that makes sense.

This brochure will be used in emails but mostly in print form so it needs to be designed print-ready but in a readable format that we can also send via email.

Here are some things that might help, including attachments:
Our company website: http://corvenwealth.com.au

NOTE
In the New Corporate Brochure Content attachment, the pages have been laid out with printing in mind. So pages 1-3 in the PDF are for the "inside" of the brochure, pages 4-6 are for the "outside" of the brochure. So the front page would be page 6 from the PDF, and the back page would be page 4.

Target Market(s)

Australian couples and singles generally over 45 years old who are seeking financial advice

Industry/Entity Type

Financial Planning

Font styles to use
Sans Serif

Requirements
Must have
• Print-ready for 3 double sided A4 pages (6 pages in total with a trifold)
• Our company logo + other graphics (all in 'Must Use' graphics folder)
• The red colour that's in our logo.
• White background - clean aesthetic.
• Our financial planning process graphic can be kept as is or re-designed to suit space.
Should not have
• Title 'Corporate Brochure'

```html
<!DOCTYPE html>
<html lang="en">
<head>
<meta charset="utf-8">
<title>Corven Wealth – Financial Planning Process</title>
<link href="https://fonts.googleapis.com/css2?family=Roboto:ital,wght@0,400;0,500;0,700;1,500;1,700&family=Pathway+Gothic+One&display=swap" rel="stylesheet">
<style>
  :root {
    --red: #ef5340;
    --ink: #333333;
    --body: #4a4a4a;
    --muted: #777777;
    --panel-left: #f4f4f4;
    --panel-mid: #f1f1f1;
    --panel-right: #e7e7e7;
    --backdrop: #cfcfcf;
    --white: #ffffff;
    --icon: #666666;
  }
  * { margin: 0; padding: 0; box-sizing: border-box; }
  html, body { width: 1200px; height: 720px; overflow: hidden; }
  body { background: var(--backdrop); font-family: 'Roboto', sans-serif; position: relative; }

  .spread {
    position: absolute; left: 18px; top: 86px;
    width: 1397px; height: 657px;
    transform: scale(0.8332); transform-origin: 0 0;
    box-shadow: 0 6px 18px rgba(0,0,0,.25);
  }
  .panel { position: absolute; top: 0; height: 657px; }
  .panel--adviser { left: 0; width: 466px; background: var(--panel-left); overflow: hidden; }
  .panel--steps { left: 466px; width: 465px; background: var(--panel-mid); }
  .panel--process { left: 931px; width: 466px; background: linear-gradient(90deg, #e2e2e2, var(--panel-right) 20%, #ececec); }

  .adviser-portrait {
    position: absolute; left: 150px; top: 0; width: 316px; height: 657px;
    background: linear-gradient(180deg, #e9e9e9 0%, #dcdcdc 45%, #e4e4e4 100%);
    opacity: .8;
  }
  .adviser-copy { position: absolute; left: 59px; top: 50px; width: 320px; color: var(--muted); }
  .eyebrow { color: var(--red); font-size: 10px; margin-bottom: 16px; }
  .eyebrow--small { font-size: 9px; margin-bottom: 6px; }
  .about p { font-size: 7px; line-height: 10px; margin-bottom: 10px; }

  .press { position: absolute; left: 59px; top: 255px; width: 320px; display: grid;
    grid-template-columns: repeat(5, 1fr); row-gap: 10px; align-items: center; justify-items: center; }
  .press__name { font-size: 6.5px; font-weight: 700; color: var(--ink); white-space: nowrap; }
  .press__badge { width: 18px; height: 18px; background: var(--icon); }
  .press__badge--round { border-radius: 50%; }

  .questions { position: absolute; left: 59px; top: 342px; width: 320px; }
  .questions h3 { color: var(--red); font-size: 10px; font-weight: 400; margin-bottom: 14px; }
  .qa dt { font-size: 9px; color: var(--ink); margin-bottom: 8px; }
  .qa dd { font-size: 6.5px; line-height: 10px; color: var(--muted); margin-bottom: 11px; }

  .process-graphic { position: absolute; left: 0; top: 0; width: 1397px; height: 657px; }
  .person-icon { position: absolute; left: 904px; top: 197px; width: 48px; height: 122px;
    background: var(--icon); border-radius: 24px 24px 6px 6px; }

  .step { position: absolute; }
  .step__title { font-size: 17px; font-weight: 700; font-style: italic; color: var(--body); }
  .step__lead { color: var(--red); font-size: 16px; line-height: 19px; margin-top: 14px; }
  .step__body { color: var(--body); font-size: 12.5px; line-height: 15px; margin-top: 16px; }
  .step--discovery { left: 500px; top: 28px; }
  .step--discovery .step__lead { width: 245px; }
  .step--discovery .step__body { width: 170px; }
  .step--interpret { left: 500px; top: 263px; }
  .step--interpret .step__body { width: 185px; margin-top: 20px; }
  .step--commitment { left: 500px; top: 479px; width: 380px; }
  .step--commitment .step__lead { margin-top: 16px; }
  .step--commitment .step__body { margin-top: 12px; }
  .step--followup { left: 990px; top: 419px; width: 366px; text-align: right; }
  .step--followup .step__lead { font-size: 15px; margin-top: 10px; }
  .step--followup .step__body { margin-top: 14px; }
  .step--followup .step__body + .step__body { margin-top: 14px; }

  .process-title { position: absolute; left: 1017px; top: 62px; color: var(--white);
    font-size: 19px; font-weight: 700; letter-spacing: .2px; }
  .ring-label { position: absolute; color: var(--white); font-family: 'Pathway Gothic One', sans-serif;
    font-size: 21px; line-height: 22px; text-align: center; transform: translateX(-50%); white-space: nowrap; }
</style>
</head>
<body>
<main class="spread">
  <section class="panel panel--adviser">
    <div class="adviser-portrait" role="img" aria-label="Faded portrait of the adviser in a suit standing by a doorway"></div>
    <div class="adviser-copy">
      <h2 class="eyebrow">Meet Your Adviser</h2>
      <h3 class="eyebrow eyebrow--small">ABOUT</h3>
      <div class="about">
        <p>Marcus Hale is the Director of Corven Wealth. He was awarded the prestigious 'Adviser of the Year' accolade in 2016 by the Guild of Wealth Advisers and was selected to join the Most Trusted Advisers group as a result of outstanding feedback from his clients.</p>
        <p>Marcus has a Bachelor of Mathematics. He is an accredited SMSF Specialist Advisor, a Certified Financial Planner and one of Australia's only financial life planners.</p>
        <p>A born and bred Northern Beaches boy, he has an active interest in many sports and with two young boys, you won't see him sitting idle. Between refereeing local football matches, teaching his boys to surf or lining up a birdie putt on the golf course, when he isn't working, Marcus is 'on the go'.</p>
        <p>You may have seen him occasionally on Streamline TV's Metro News business program Money Matters Live, or quoted in publications including the Market Ledger or The Harbour Herald.</p>
      </div>
    </div>
    <div class="press" aria-label="As featured in">
      <span class="press__name">MARKET LEDGER</span>
      <span class="press__name">Harbour Herald</span>
      <span class="press__name">wise saver</span>
      <span class="press__name">THE NATIONAL</span>
      <span class="press__name">Daily Courier</span>
      <span class="press__badge press__badge--round"></span>
      <span class="press__badge press__badge--round"></span>
      <span class="press__badge"></span>
      <span class="press__badge"></span>
      <span class="press__name">FUND REVIEW</span>
      <span class="press__name">BAYSIDE AGE</span>
      <span class="press__badge press__badge--round"></span>
      <span class="press__badge"></span>
      <span class="press__badge"></span>
      <span class="press__badge"></span>
    </div>
    <div class="questions">
      <h3>5 QUESTIONS FOR MARCUS</h3>
      <dl class="qa">
        <dt>What do you love most about your career?</dt>
        <dd>Being able to help people live their ideal life and helping them understand how to use money.</dd>
        <dt>What is your experience as a financial adviser?</dt>
        <dd>We always worked in a small, self-licensed business so my experience is more around solving clients' most pressing financial challenges rather than meeting a sales target. Boutique firms tend to work differently to banks and large institutions.</dd>
        <dt>What type of clients do you specialise in?</dt>
        <dd>We look after 3 types of clients. Firstly, people who are suddenly single and face making financial decisions alone, often for the first time. Secondly, those who are winding down and don't want to spend their non-working years trying to teach themselves finance. And thirdly, couples with good incomes but no time to dedicate to their own financial wellbeing.</dd>
        <dt>What are the things you value most in life?</dt>
        <dd>9 hours of sleep each night and weekends with family.</dd>
        <dt>If you won the lottery tomorrow, how would you live your life?</dt>
        <dd>I would continue to align my values with my actions. And buy a better second-hand surfboard.</dd>
      </dl>
    </div>
  </section>

  <section class="panel panel--steps"></section>
  <section class="panel panel--process"></section>

  <svg class="process-graphic" viewBox="0 0 1397 657" aria-hidden="true">
    <rect x="927" y="27" width="470" height="96" fill="var(--red)"/>
    <circle cx="927" cy="256" r="229" fill="var(--red)"/>
    <circle cx="927" cy="256" r="94" fill="var(--white)"/>
  </svg>
  <div class="person-icon" role="img" aria-label="Person icon at the centre of the process ring"></div>

  <h1 class="process-title">OUR FINANCIAL PLANNING PROCESS</h1>
  <div class="ring-label" style="left:925px;top:75px">Step One<br>Discovery</div>
  <div class="ring-label" style="left:1079px;top:224px">Step Two<br>Interpret</div>
  <div class="ring-label" style="left:925px;top:388px">Step Three<br>Mutual Commitment</div>
  <div class="ring-label" style="left:763px;top:230px">Step Four<br>90 Day Follow-Up</div>

  <article class="step step--discovery">
    <h2 class="step__title">Step1: Discovery</h2>
    <p class="step__lead">No two human beings are exactly alike and similarly, no two financial plans are the same.</p>
    <p class="step__body">This is the time where we listen and learn about you; your values, your aspirations, your financial goals. We work with you to determine how we can help reach your goals. We look at where you</p>
  </article>
  <article class="step step--interpret">
    <h2 class="step__title">Steps2: Interpret</h2>
    <p class="step__lead">Check that everything<br>is in place.</p>
    <p class="step__body">We meet to recap the results you can expect and answer your questions. We also understand that things can change. That's why we review and adjust your financial plan as necessary. We're on your side.</p>
  </article>
  <article class="step step--commitment">
    <h2 class="step__title">Steps3: Mutual Commitment</h2>
    <p class="step__lead">Let's Implement</p>
    <p class="step__body">We work with you to implement your plan over the areas relevant to your individual goal. We meet with you to outline the results you can expect in the short and long term path to your financial security, and we keep you abreast of the big picture. This is the exciting part!</p>
  </article>
  <article class="step step--followup">
    <h2 class="step__title">Steps4: 90 Day Follow-Up</h2>
    <p class="step__lead">Did we hear you correctly?</p>
    <p class="step__body">We want to make sure we understand you. So we send you an interpretation paper with a complete diagnosis of your current financial situation and our recommendations on the strategy required to reach your goals. This plan will form the foundation of how we work together</p>
    <p class="step__body">Corven Wealth prides itself on lifelong relationships and we encourage you to take the time necessary to be comfortable with all aspects of our proposal prior to taking the next step</p>
  </article>
</main>
</body>
</html>
```